Creative Challenge - Disruptive Digital Construction Business needs an Application Design

We need an application design (4 screens).
The app will offer easy-to-use an interactive course to illustrate the latest technology to construction professionals. Kindly find the attachments.
Updates

I have just posted the contest and the deadline is tomorrow!! Please give me my original 7 days back.

Need extra days to review

Target Market(s)

Construction professionals, aged from 22 to 36, who want to learn new disruptive technologies in construction.

Colors
e667a6
b868aa
33a6d7

Requirements
Must have
• The name of the app, Velmiro, stands for “Virtual Engineering Leaders”. The user is a Velmiro, who would transform the digital construction industry. We want a design that gives that feel to the users.

```html
<!DOCTYPE html>
<html lang="en">
<head>
<meta charset="utf-8">
<title>Velmiro – Navigation Drawer</title>
<link href="https://fonts.googleapis.com/css2?family=Inter:wght@400;500;600;700&display=swap" rel="stylesheet">
<style>
  :root {
    --page-bg: #ffffff;
    --header-navy: #24365f;
    --body-dim: #5f506b;
    --card-dim: #6a5a74;
    --tile-navy: #2b4673;
    --menu-btn: #8a6c8c;
    --menu-icon: #2c2a45;
    --drawer-bg: #ffffff;
    --name-ink: #2d1b45;
    --phone-ink: #6b6478;
    --item-ink: #3f3a4b;
    --icon-ink: #5f6170;
    --divider: #d4d4d8;
    --logout: #ef5aa4;
    --status-ink: #b9b6cc;
  }
  * { box-sizing: border-box; margin: 0; padding: 0; }
  html, body {
    width: 1200px; height: 1000px; overflow: hidden;
    background: var(--page-bg);
    font-family: "Inter", Arial, sans-serif;
  }
  .screen {
    position: absolute; left: 388px; top: 42px;
    width: 423px; height: 916px; overflow: hidden;
    background: var(--body-dim);
    box-shadow: 0 18px 50px rgba(40, 30, 60, 0.16);
  }
  .app-header {
    position: absolute; left: 0; top: 0; width: 100%; height: 191px;
    background: var(--header-navy);
  }
  .status-bar {
    position: absolute; left: 16px; top: 16px;
    font-size: 12px; color: var(--status-ink); letter-spacing: 0.5px;
  }
  .menu-button {
    position: absolute; left: 23px; top: 66px;
    width: 46px; height: 46px; border-radius: 50%;
    background: var(--menu-btn);
    display: flex; align-items: center; justify-content: center;
  }
  .course-card {
    position: absolute; left: 22px; width: 140px; height: 108px;
    background: var(--card-dim); border-radius: 4px;
  }
  .course-card .tile-icon {
    position: absolute; left: 29px; top: 21px;
    width: 66px; height: 66px; border-radius: 50%;
    background: var(--tile-navy);
  }
  .drawer {
    position: absolute; left: 89px; top: 0; width: 334px; height: 100%;
    background: var(--drawer-bg);
    box-shadow: -6px 0 20px rgba(0,0,0,0.08);
  }
  .avatar {
    position: absolute; left: 104px; top: 85px;
    width: 126px; height: 126px; border-radius: 50%;
    border: 5px solid #fff;
    background: radial-gradient(circle at 55% 60%, #8a9896 0%, #4b5a4c 45%, #1f2a1e 100%);
    box-shadow: 0 2px 10px rgba(0,0,0,0.15);
  }
  .user-name {
    position: absolute; left: 0; top: 227px; width: 100%;
    text-align: center; font-size: 24px; font-weight: 700; color: var(--name-ink);
  }
  .user-phone {
    position: absolute; left: 0; top: 265px; width: 100%;
    text-align: center; font-size: 17px; color: var(--phone-ink);
  }
  .divider {
    position: absolute; left: 0; top: 319px; width: 100%; height: 2px;
    background: var(--divider);
  }
  .drawer-menu { position: absolute; left: 67px; top: 359px; list-style: none; }
  .drawer-menu li {
    display: flex; align-items: center; height: 59.5px;
    font-size: 19px; color: var(--item-ink);
  }
  .drawer-menu svg { width: 28px; height: 28px; margin-right: 14px; fill: var(--icon-ink); }
  .logout {
    position: absolute; left: 0; bottom: 0; width: 100%; height: 70px;
    background: var(--logout); color: #fff;
    font-size: 19px; font-weight: 700;
    display: flex; align-items: center; justify-content: center;
  }
</style>
</head>
<body>
<div class="screen">
  <header class="app-header">
    <div class="status-bar">●●●○○ VL</div>
    <div class="menu-button">
      <svg width="18" height="14" viewBox="0 0 18 14"><g fill="var(--menu-icon)"><rect y="1" width="18" height="2"/><rect y="6" width="18" height="2"/><rect y="11" width="18" height="2"/></g></svg>
    </div>
  </header>

  <div class="course-card" style="top:210px"><div class="tile-icon"></div></div>
  <div class="course-card" style="top:338px"><div class="tile-icon"></div></div>
  <div class="course-card" style="top:468px"><div class="tile-icon"></div></div>
  <div class="course-card" style="top:595px"><div class="tile-icon"></div></div>
  <div class="course-card" style="top:724px"><div class="tile-icon"></div></div>
  <div class="course-card" style="top:852px"><div class="tile-icon"></div></div>

  <nav class="drawer">
    <div class="avatar" role="img" aria-label="Profile photo of the user"></div>
    <div class="user-name">Samir</div>
    <div class="user-phone">+91 7704218856</div>
    <div class="divider"></div>
    <ul class="drawer-menu">
      <li><svg viewBox="0 0 24 24"><path d="M12 1a11 11 0 1 0 0 22 11 11 0 0 0 0-22zm0 4a4 4 0 1 1 0 8 4 4 0 0 1 0-8zm0 16a9 9 0 0 1-6.6-2.9c1.3-2 3.8-3.1 6.6-3.1s5.3 1.1 6.6 3.1A9 9 0 0 1 12 21z"/></svg>Profile</li>
      <li><svg viewBox="0 0 24 24"><path d="M12 21.5 3.4 13A5.6 5.6 0 0 1 12 5.8 5.6 5.6 0 0 1 20.6 13z"/></svg>My Favourite</li>
      <li><svg viewBox="0 0 24 24"><path d="M10.5 2a8.5 8.5 0 0 1 6.8 13.6l4.8 4.8-2 2-4.8-4.8A8.5 8.5 0 1 1 10.5 2zm0 2.8a5.7 5.7 0 1 0 0 11.4 5.7 5.7 0 0 0 0-11.4z"/></svg>Search</li>
      <li><svg viewBox="0 0 24 24"><circle cx="12" cy="12" r="11"/><path d="M9 9.2a3 3 0 1 1 4.2 2.7c-.8.4-1.2 1-1.2 1.8v.6" stroke="#fff" stroke-width="2.2" fill="none" stroke-linecap="round"/><circle cx="12" cy="17.6" r="1.3" fill="#fff"/></svg>About the App</li>
      <li><svg viewBox="0 0 24 24"><path d="M12 2a9 9 0 0 0-9 9v5a3 3 0 0 0 3 3h1v-8H5a7 7 0 0 1 14 0h-2v8h2v1a2 2 0 0 1-2 2h-3v1.6h3a3.6 3.6 0 0 0 3.6-3.6v-1A3 3 0 0 0 21 16v-5a9 9 0 0 0-9-9z"/></svg>Contact Us</li>
      <li><svg viewBox="0 0 24 24"><circle cx="13" cy="7" r="4.5"/><path d="M4 22c0-5 4-8 9-8s9 3 9 8z"/><circle cx="6" cy="10" r="2.6"/><path d="M1 18c0-3 2.2-4.8 5-4.8 1 0 1.8.2 2.5.6C6.8 15 5.8 16.4 5.5 18z"/></svg>About the Authors</li>
    </ul>
    <div class="logout">LOGOUT</div>
  </nav>
</div>
</body>
</html>
```